RT Pemberly Electric Yard Sign

Looking to have a yard sign designed that we can place at projects we are working on. Most likely will be 18" H x 24" W but flexible that we can increase the size if necessary. It should include our logo, our phone # 609-555-0147, website rtpemberlyelectric-example.com and slogan, built on integrity, driven by excellence. Colors should match our brand.

```html
<!DOCTYPE html>
<html lang="en">
<head>
<meta charset="utf-8">
<title>RT Pemberly Electric – Yard Sign</title>
<link rel="stylesheet" href="https://fonts.googleapis.com/css2?family=Orbitron:wght@800;900&family=Open+Sans:wght@700&family=Source+Sans+3:wght@700&display=swap">
<style>
  :root {
    --navy: #0c3a6d;
    --red: #e11b2f;
    --white: #ffffff;
    --backdrop: #e9ebee;
  }
  * { box-sizing: border-box; margin: 0; padding: 0; }
  html, body {
    width: 1200px;
    height: 916px;
    overflow: hidden;
    background: var(--backdrop);
  }
  .yard-sign {
    position: absolute;
    left: 56px;
    top: 48px;
    width: 1088px;
    height: 820px;
    background: var(--white);
    border: 20px solid var(--navy);
    text-align: center;
  }
  .brand-mark {
    position: absolute;
    left: 50%;
    top: 62px;
    width: 124px;
    height: 124px;
    margin-left: -62px;
    border-radius: 50%;
    background: var(--red);
  }
  .brand-name {
    position: absolute;
    left: 0; right: 0;
    top: 222px;
    font-family: "Orbitron", sans-serif;
    font-weight: 900;
    font-size: 80px;
    line-height: 1;
    color: var(--red);
    letter-spacing: 0.02em;
    white-space: nowrap;
  }
  .trade {
    position: absolute;
    left: 0; right: 0;
    top: 334px;
    font-family: "Open Sans", sans-serif;
    font-weight: 700;
    font-size: 40px;
    line-height: 1;
    letter-spacing: 0.44em;
    padding-left: 0.44em;
    color: var(--navy);
    white-space: nowrap;
  }
  .divider {
    position: absolute;
    left: 33px;
    width: 982px;
    height: 18px;
  }
  .divider--upper { top: 408px; }
  .divider--lower { top: 556px; }
  .slogan {
    position: absolute;
    left: 0; right: 0;
    top: 462px;
    font-family: "Source Sans 3", sans-serif;
    font-weight: 700;
    font-size: 51px;
    line-height: 1;
    color: var(--navy);
    white-space: nowrap;
  }
  .phone, .website {
    position: absolute;
    left: 0; right: 0;
    font-family: "Orbitron", sans-serif;
    font-weight: 800;
    line-height: 1;
    color: var(--red);
    -webkit-text-stroke: 2px var(--navy);
    paint-order: stroke fill;
    white-space: nowrap;
  }
  .phone {
    top: 610px;
    font-size: 60px;
    letter-spacing: 0.08em;
  }
  .website {
    top: 700px;
    font-size: 34px;
    letter-spacing: 0.02em;
  }
</style>
</head>
<body>
  <main class="yard-sign">
    <span class="brand-mark" aria-hidden="true"></span>
    <h1 class="brand-name">R.T. PEMBERLY</h1>
    <p class="trade">Electrical Contractor</p>

    <svg class="divider divider--upper" viewBox="0 0 982 18" aria-hidden="true">
      <polygon points="0,7 14,2 968,2 982,7 968,5 14,5" fill="var(--red)"/>
      <rect x="14" y="7" width="954" height="7" fill="var(--navy)"/>
    </svg>

    <p class="slogan">Built on integrity, driven by excellence</p>

    <svg class="divider divider--lower" viewBox="0 0 982 18" aria-hidden="true">
      <rect x="14" y="3" width="954" height="7" fill="var(--navy)"/>
      <polygon points="0,16 14,11 968,11 982,16 968,13 14,13" fill="var(--red)"/>
    </svg>

    <p class="phone">609-555-0147</p>
    <p class="website">RTPEMBERLYELECTRIC-EXAMPLE.COM</p>
  </main>
</body>
</html>
```